Round Label for 100% natural deodorant tin

We are just about to launch our luxuriously, brilliant, eco friendly little company 'Perrin Waldeck', named after my 10 month old son. Our 'flagship' line of products will be natural cream deodorants in a range of different natural scents.
Currently we will be using 60ml aluminum tins to package the product and we will need two labels (approx. 2.5" each) top and bottom of the tin. The top label needs to scream, luxury, eco friendly, exciting, professional and it must be immediately obvious that we are selling a deodorant cream!
This product does not contain any harmful chemicals or environment polluting ingredients ........its simply heavenly on the skin and it works! The bottom label can be simple black and white with instructions and ingredients.
It would be nice to somehow incorporate our logo or simply the leaf on our logo for the top label somehow.
Updates

Designers please keep in mind that print shops require that no text appear within 3mm from outer edge of circle. Thanks so much.

Target Market(s)

Aimed at teenagers to middle aged people. The packaging will hopefully be unisex in style and be bright and fresh!

Industry/Entity Type

Environment

Requirements
Must have
• The top label must incorporate;
60ml
Natural Cream Deodorant
Varieties for each tin;
lavender, unscented, citrus, cypress.
The bottom label simply needs instructions and the ingredients.
Nice to have
• It would be nice to try and use our logo in the design.
Should not have
• Should NOT be boring and sensible!

```html
<!DOCTYPE html>
<html lang="en">
<head>
<meta charset="utf-8">
<title>Perrin Waldeck – Natural Deodorant Tin Labels</title>
<link rel="stylesheet" href="https://fonts.googleapis.com/css2?family=Josefin+Sans:wght@400;600;700&family=Montserrat:wght@700&display=swap">
<style>
  :root {
    --ring-green: #84ad86;
    --brand-teal: #2f5b55;
    --ink: #111111;
    --muted: #9a9a9a;
    --paper: #ffffff;
    --unscented: #d5cda6;
    --lavender: #9b4fb4;
    --cypress: #2b94c1;
    --citrus: #eea148;
  }
  html, body {
    margin: 0;
    padding: 0;
    overflow: hidden;
    background: var(--paper);
  }
  .sheet {
    position: relative;
    width: 707px;
    height: 1200px;
    overflow: hidden;
    background: var(--paper);
    font-family: "Josefin Sans", sans-serif;
  }
  .defs { position: absolute; width: 0; height: 0; }

  /* Top label */
  .top-label {
    position: absolute;
    left: 38px;
    width: 300px;
    height: 300px;
  }
  .ring { fill: var(--ring-green); }
  .ring-text {
    font-family: "Josefin Sans", sans-serif;
    font-weight: 700;
    font-size: 19px;
    letter-spacing: 3px;
    fill: var(--paper);
  }
  .brand-name {
    font-family: "Montserrat", sans-serif;
    font-weight: 700;
    font-size: 22px;
    letter-spacing: 1px;
    fill: var(--brand-teal);
    text-anchor: middle;
  }
  .variety-name {
    font-family: "Montserrat", sans-serif;
    font-weight: 700;
    font-size: 25px;
    letter-spacing: 3px;
    fill: var(--paper);
    text-anchor: middle;
  }
  .volume {
    font-family: "Josefin Sans", sans-serif;
    font-size: 11px;
    letter-spacing: 1px;
    fill: var(--muted);
    text-anchor: middle;
  }

  /* Bottom label */
  .bottom-label {
    position: absolute;
    left: 399px;
    width: 262px;
    height: 262px;
    border: 2px solid var(--ink);
    border-radius: 50%;
    background: radial-gradient(circle at 50% 60%, #ffffff 35%, #f1f1f1 100%);
    color: var(--ink);
    text-align: center;
    box-sizing: content-box;
    overflow: hidden;
  }
  .bottom-inner {
    position: absolute;
    left: 28px;
    right: 28px;
    top: 14px;
    font-size: 7px;
    line-height: 1.2;
  }
  .title {
    margin: 0 auto 4px;
    padding-bottom: 2px;
    width: 120px;
    border-bottom: 1px solid var(--ink);
    font-weight: 700;
    font-size: 9px;
    letter-spacing: 1px;
    line-height: 1.1;
  }
  .claims { margin: 0 0 4px; }
  .heading {
    margin: 0;
    font-weight: 700;
    font-size: 8px;
    letter-spacing: 1.4px;
  }
  .body-copy { margin: 0 0 3px; padding: 0 4px; }
  .contact {
    margin: 2px 0 4px;
    font-weight: 600;
    font-size: 7.2px;
    letter-spacing: 1px;
  }
  .maker-label {
    display: block;
    margin: 0 0 2px 18px;
    text-align: left;
    font-weight: 700;
    font-size: 7.4px;
    letter-spacing: 1.1px;
  }
  .maker {
    display: flex;
    align-items: flex-end;
    justify-content: center;
    gap: 10px;
  }
  .maker-name {
    font-family: "Montserrat", sans-serif;
    font-weight: 700;
    font-size: 6px;
    color: var(--brand-teal);
    line-height: 1.1;
    width: 34px;
  }
  .badge {
    display: flex;
    flex-direction: column;
    align-items: center;
    font-size: 4.8px;
    font-weight: 700;
    line-height: 1;
  }
  .badge-shape {
    width: 17px;
    height: 17px;
    border-radius: 50%;
    border: 1px solid var(--ink);
    margin-bottom: 2px;
  }
  .jar-icon { width: 26px; height: 21px; }
</style>
</head>
<body>
<main class="sheet">

  <svg class="defs" aria-hidden="true">
    <defs>
      <path id="arc-top" d="M -123,0 A 123 123 0 0 1 123,0"/>
      <path id="arc-bottom" d="M -137,0 A 137 137 0 0 0 137,0"/>
      <clipPath id="face-clip"><circle r="116"/></clipPath>
      <linearGradient id="tint-unscented" x1="0" y1="0" x2="1" y2="1">
        <stop offset="0" stop-color="#f3eed9"/>
        <stop offset="0.5" stop-color="#e3eedf"/>
        <stop offset="1" stop-color="#f7f3e6"/>
      </linearGradient>
      <linearGradient id="tint-lavender" x1="0" y1="0" x2="1" y2="1">
        <stop offset="0" stop-color="#ecdff2"/>
        <stop offset="0.5" stop-color="#e0eede"/>
        <stop offset="1" stop-color="#f1e6f5"/>
      </linearGradient>
      <linearGradient id="tint-cypress" x1="0" y1="0" x2="1" y2="1">
        <stop offset="0" stop-color="#d9ebf5"/>
        <stop offset="0.5" stop-color="#e0eede"/>
        <stop offset="1" stop-color="#dcedf7"/>
      </linearGradient>
      <linearGradient id="tint-citrus" x1="0" y1="0" x2="1" y2="1">
        <stop offset="0" stop-color="#fbe8d2"/>
        <stop offset="0.5" stop-color="#e3eedf"/>
        <stop offset="1" stop-color="#fcecd9"/>
      </linearGradient>
    </defs>
  </svg>

  <!-- Unscented top -->
  <svg class="top-label" style="top:0" viewBox="-150 -150 300 300">
    <circle class="ring" r="144"/>
    <circle r="116" fill="#ffffff"/>
    <g clip-path="url(#face-clip)">
      <rect role="img" aria-label="Faint leaf pattern in soft beige and green" x="-116" y="-116" width="232" height="144" fill="url(#tint-unscented)"/>
      <rect x="-116" y="28" width="232" height="40" fill="var(--unscented)"/>
    </g>
    <text class="brand-name" y="-6">PERRIN</text>
    <text class="brand-name" y="20">WALDECK</text>
    <text class="variety-name" y="57">UNSCENTED</text>
    <text class="volume" y="90">60ML</text>
    <text class="ring-text"><textPath href="#arc-top" startOffset="50%" text-anchor="middle">NATURAL DEODORANT</textPath></text>
    <text class="ring-text"><textPath href="#arc-bottom" startOffset="50%" text-anchor="middle">DEODORANT NATUREL</textPath></text>
  </svg>

  <!-- Lavender top -->
  <svg class="top-label" style="top:294px" viewBox="-150 -150 300 300">
    <circle class="ring" r="144"/>
    <circle r="116" fill="#ffffff"/>
    <g clip-path="url(#face-clip)">
      <rect role="img" aria-label="Faint leaf pattern in soft lilac and green" x="-116" y="-116" width="232" height="144" fill="url(#tint-lavender)"/>
      <rect x="-116" y="28" width="232" height="40" fill="var(--lavender)"/>
    </g>
    <text class="brand-name" y="-6">PERRIN</text>
    <text class="brand-name" y="20">WALDECK</text>
    <text class="variety-name" y="57">LAVENDER</text>
    <text class="volume" y="90">60ML</text>
    <text class="ring-text"><textPath href="#arc-top" startOffset="50%" text-anchor="middle">NATURAL DEODORANT</textPath></text>
    <text class="ring-text"><textPath href="#arc-bottom" startOffset="50%" text-anchor="middle">DEODORANT NATUREL</textPath></text>
  </svg>

  <!-- Cypress top -->
  <svg class="top-label" style="top:590px" viewBox="-150 -150 300 300">
    <circle class="ring" r="144"/>
    <circle r="116" fill="#ffffff"/>
    <g clip-path="url(#face-clip)">
      <rect role="img" aria-label="Faint leaf pattern in soft sky blue and green" x="-116" y="-116" width="232" height="144" fill="url(#tint-cypress)"/>
      <rect x="-116" y="28" width="232" height="40" fill="var(--cypress)"/>
    </g>
    <text class="brand-name" y="-6">PERRIN</text>
    <text class="brand-name" y="20">WALDECK</text>
    <text class="variety-name" y="57">CYPRESS</text>
    <text class="volume" y="90">60ML</text>
    <text class="ring-text"><textPath href="#arc-top" startOffset="50%" text-anchor="middle">NATURAL DEODORANT</textPath></text>
    <text class="ring-text"><textPath href="#arc-bottom" startOffset="50%" text-anchor="middle">DEODORANT NATUREL</textPath></text>
  </svg>

  <!-- Citrus top -->
  <svg class="top-label" style="top:888px" viewBox="-150 -150 300 300">
    <circle class="ring" r="144"/>
    <circle r="116" fill="#ffffff"/>
    <g clip-path="url(#face-clip)">
      <rect role="img" aria-label="Faint leaf pattern in soft peach and green" x="-116" y="-116" width="232" height="144" fill="url(#tint-citrus)"/>
      <rect x="-116" y="28" width="232" height="40" fill="var(--citrus)"/>
    </g>
    <text class="brand-name" y="-6">PERRIN</text>
    <text class="brand-name" y="20">WALDECK</text>
    <text class="variety-name" y="57">CITRUS</text>
    <text class="volume" y="90">60ML</text>
    <text class="ring-text"><textPath href="#arc-top" startOffset="50%" text-anchor="middle">NATURAL DEODORANT</textPath></text>
    <text class="ring-text"><textPath href="#arc-bottom" startOffset="50%" text-anchor="middle">DEODORANT NATUREL</textPath></text>
  </svg>

  <!-- Unscented bottom -->
  <section class="bottom-label" style="top:17px" role="img" aria-label="Faint grey leaf pattern behind label text">
    <div class="bottom-inner">
      <p class="title">100% NATURAL<br>UNSCENTED<br>DEODORANT CREAM</p>
      <p class="claims">*Highly effective *Kind to the skin *4-6 month's supply<br>*No Aluminium *No GMO *No artificial anything</p>
      <p class="heading">INSTRUCTIONS</p>
      <p class="body-copy">Apply a pea sized amount with finger tips on to freshly washed and dry arm pits, for all day long freshness.</p>
      <p class="heading">INGREDIENTS</p>
      <p class="body-copy">Arrowroot (Maranta arundinaceae), Virgin coconut oil (cocos nucifera), castor oil (Ricinus communis), baking soda (sodium bicarbonate), bees wax (Cera alba). 100% natural. May cause slight irritation on freshly shaved arm pits.</p>
      <p class="contact">HELLO@PERRINWALDECK.EXAMPLE<br>MADE IN GREAT BRITAIN</p>
      <span class="maker-label">HANDMADE BY</span>
      <div class="maker">
        <span class="maker-name">PERRIN WALDECK</span>
        <span class="badge"><span class="badge-shape"></span>NOT TESTED<br>ON ANIMALS</span>
        <svg class="jar-icon" viewBox="0 0 30 24" aria-hidden="true"><path d="M8 4 L22 1" stroke="#111" fill="none"/><rect x="3" y="8" width="24" height="14" rx="2" fill="none" stroke="#111" stroke-width="1.4"/><text x="15" y="19" font-size="7" font-weight="700" text-anchor="middle" font-family="Josefin Sans, sans-serif">7M</text></svg>
      </div>
    </div>
  </section>

  <!-- Lavender bottom -->
  <section class="bottom-label" style="top:311px" role="img" aria-label="Faint grey leaf pattern behind label text">
    <div class="bottom-inner">
      <p class="title">100% NATURAL<br>LAVENDER<br>DEODORANT CREAM</p>
      <p class="claims">*Highly effective *Kind to the skin *4-6 month's supply<br>*No Aluminium *No GMO *No artificial anything</p>
      <p class="heading">INSTRUCTIONS</p>
      <p class="body-copy">Apply a pea sized amount with finger tips on to freshly washed and dry arm pits, for all day long freshness.</p>
      <p class="heading">INGREDIENTS</p>
      <p class="body-copy">Arrowroot (Maranta arundinaceae), Virgin coconut oil (cocos nucifera), castor oil (Ricinus communis), baking soda (sodium bicarbonate), bees wax (Cera alba), Lavender essential oil (Lavendula angustifolia). 100% natural. May cause slight irritation on freshly shaved arm pits.</p>
      <p class="contact">HELLO@PERRINWALDECK.EXAMPLE<br>MADE IN GREAT BRITAIN</p>
      <span class="maker-label">HANDMADE BY</span>
      <div class="maker">
        <span class="maker-name">PERRIN WALDECK</span>
        <span class="badge"><span class="badge-shape"></span>NOT TESTED<br>ON ANIMALS</span>
        <svg class="jar-icon" viewBox="0 0 30 24" aria-hidden="true"><path d="M8 4 L22 1" stroke="#111" fill="none"/><rect x="3" y="8" width="24" height="14" rx="2" fill="none" stroke="#111" stroke-width="1.4"/><text x="15" y="19" font-size="7" font-weight="700" text-anchor="middle" font-family="Josefin Sans, sans-serif">7M</text></svg>
      </div>
    </div>
  </section>

  <!-- Cypress bottom -->
  <section class="bottom-label" style="top:607px" role="img" aria-label="Faint grey leaf pattern behind label text">
    <div class="bottom-inner">
      <p class="title">100% NATURAL<br>CYPRESS<br>DEODORANT CREAM</p>
      <p class="claims">*Highly effective *Kind to the skin *4-6 month's supply<br>*No Aluminium *No GMO *No artificial anything</p>
      <p class="heading">INSTRUCTIONS</p>
      <p class="body-copy">Apply a pea sized amount with finger tips on to freshly washed and dry arm pits, for all day long freshness.</p>
      <p class="heading">INGREDIENTS</p>
      <p class="body-copy">Arrowroot (Maranta arundinaceae), Virgin coconut oil (cocos nucifera), castor oil (Ricinus communis), baking soda (sodium bicarbonate), bees wax (Cera alba), Cedarwood (Cedrus Atlantica), Patchouli (Pogostemon cablin), Cypress (Callitris intratropica). 100% natural. May cause slight irritation on freshly shaved arm pits.</p>
      <p class="contact">HELLO@PERRINWALDECK.EXAMPLE<br>MADE IN GREAT BRITAIN</p>
      <span class="maker-label">HANDMADE BY</span>
      <div class="maker">
        <span class="maker-name">PERRIN WALDECK</span>
        <span class="badge"><span class="badge-shape"></span>NOT TESTED<br>ON ANIMALS</span>
        <svg class="jar-icon" viewBox="0 0 30 24" aria-hidden="true"><path d="M8 4 L22 1" stroke="#111" fill="none"/><rect x="3" y="8" width="24" height="14" rx="2" fill="none" stroke="#111" stroke-width="1.4"/><text x="15" y="19" font-size="7" font-weight="700" text-anchor="middle" font-family="Josefin Sans, sans-serif">7M</text></svg>
      </div>
    </div>
  </section>

  <!-- Citrus bottom -->
  <section class="bottom-label" style="top:905px" role="img" aria-label="Faint grey leaf pattern behind label text">
    <div class="bottom-inner">
      <p class="title">100% NATURAL<br>CITRUS<br>DEODORANT CREAM</p>
      <p class="claims">*Highly effective *Kind to the skin *4-6 month's supply<br>*No Aluminium *No GMO *No artificial anything</p>
      <p class="heading">INSTRUCTIONS</p>
      <p class="body-copy">Apply a pea sized amount with finger tips on to freshly washed and dry arm pits, for all day long freshness.</p>
      <p class="heading">INGREDIENTS</p>
      <p class="body-copy">Arrowroot (Maranta arundinaceae), Virgin coconut oil (cocos nucifera), castor oil (Ricinus communis), baking soda (sodium bicarbonate), bees wax (Cera alba), essential oils of Bergamot (citrus Bergamia), Pink Grapefruit (citrus Racemosa), Orange (citrus Sinensis). 100% natural. Citrus oils may cause sun sensitivity: use caution. May cause slight irritation on freshly shaved arm pits.</p>
      <p class="contact">HELLO@PERRINWALDECK.EXAMPLE<br>MADE IN GREAT BRITAIN</p>
      <span class="maker-label">HANDMADE BY</span>
      <div class="maker">
        <span class="maker-name">PERRIN WALDECK</span>
        <span class="badge"><span class="badge-shape"></span>NOT TESTED<br>ON ANIMALS</span>
        <svg class="jar-icon" viewBox="0 0 30 24" aria-hidden="true"><path d="M8 4 L22 1" stroke="#111" fill="none"/><rect x="3" y="8" width="24" height="14" rx="2" fill="none" stroke="#111" stroke-width="1.4"/><text x="15" y="19" font-size="7" font-weight="700" text-anchor="middle" font-family="Josefin Sans, sans-serif">7M</text></svg>
      </div>
    </div>
  </section>

</main>
</body>
</html>
```